Wine Cruise Flyer

Please design a flyer to promote wine-themed river cruises to winery owners. The target audience are high-end wineries. The purpose is to show them the benefits of organizing wine-themed river cruises to the members of their wine clubs and others who know them and buy their wine. Orvel Riverlines is the cruise line they would travel on. Brindlecove Travel is the travel agency that would organize the trip on behalf of the wineries.

```html
<!DOCTYPE html>
<html lang="en">
<head>
<meta charset="utf-8">
<title>Wine Cruise Flyer – Brindlecove Travel</title>
<link rel="stylesheet" href="https://fonts.googleapis.com/css2?family=Playfair+Display:wght@700&family=Lato:wght@400;700&display=swap">
<style>
  :root{
    --navy:#2e3550;
    --navy-deep:#242a41;
    --slate:#8b8d95;
    --slate-light:#c7c8cd;
    --mist:#e4e5e8;
    --paper:#ffffff;
    --canvas:#d3d3d5;
    --heading:"Playfair Display", Georgia, serif;
    --body:"Lato", Arial, sans-serif;
  }
  *{box-sizing:border-box;margin:0;padding:0}
  html,body{width:1200px;height:903px;overflow:hidden}
  body{background:var(--canvas);font-family:var(--body);position:relative}

  .spread{position:absolute;left:270px;width:660px;height:427px;overflow:hidden;background:var(--paper);box-shadow:0 4px 14px rgba(0,0,0,.18)}
  .spread--inside{top:16px}
  .spread--outside{top:459px}
  .fold{position:absolute;left:329px;top:0;width:2px;height:100%;background:linear-gradient(90deg,rgba(0,0,0,.08),rgba(0,0,0,0));z-index:9}
  .decor{position:absolute;left:0;top:0}
  .abs{position:absolute}

  .photo{position:absolute}
  .photo--food{background:radial-gradient(ellipse at 45% 55%,#d8583a 0%,#e89a4a 30%,#3a3a3c 70%,#1f1f22 100%)}
  .photo--town{background:linear-gradient(180deg,#b9cde0 0%,#d9e2e8 35%,#7d8f6a 55%,#5b6f4f 75%,#8aa3b6 100%)}
  .photo--suite{background:linear-gradient(160deg,#f1ece4 0%,#d8cfc2 50%,#a99a86 100%)}
  .photo--dining{background:linear-gradient(160deg,#e9e4dc 0%,#c59a72 50%,#7d5a3e 100%)}
  .photo--pool{background:linear-gradient(180deg,#c5dbe6 0%,#7fb6c9 40%,#2f8fae 70%,#d7d2c8 100%)}
  .photo--party{background:linear-gradient(180deg,#cfd8de 0%,#9cb3c2 30%,#37a6c8 55%,#c9a58c 75%,#4a4a4f 100%)}
  .photo--river{background:linear-gradient(180deg,#c7d6e2 0%,#a9bfcf 30%,#6e8a6a 55%,#7e9fb5 80%,#5e7a55 100%)}
  .photo--vines{background:linear-gradient(180deg,#b7c7b0 0%,#7f9b4e 40%,#5b7a32 70%,#8d8a52 100%)}
  .photo--church{background:linear-gradient(180deg,#cfdbe4 0%,#b9c6cf 40%,#9a8a70 60%,#6f7a58 100%)}

  /* inside left */
  .included__title{left:16px;top:58px;font:700 19px/1 var(--heading);color:var(--navy);letter-spacing:.5px}
  .included__list{left:28px;top:86px;width:282px;font-size:6.6px;line-height:1.55;color:#3c3f4a;list-style:square}
  .included__list li{margin-bottom:1px}
  .frame{position:absolute;border:4px solid var(--mist);box-shadow:0 2px 6px rgba(0,0,0,.25)}
  .food-frame{left:62px;top:182px;width:206px;height:104px}
  .voyage{left:40px;top:296px;width:262px;height:112px;background:var(--navy);border:3px solid var(--mist);display:flex}
  .voyage__text{width:112px;padding:10px 8px;color:#fff;font-size:6.8px;line-height:1.5}
  .voyage__text strong{display:block;margin-top:6px;font-size:6.2px;letter-spacing:.3px}
  .voyage .photo{position:relative;flex:1}

  /* inside right */
  .luxury{left:330px;top:0;width:330px;height:427px;background:var(--navy)}
  .luxury__title{left:348px;top:18px;font:700 19px/1 var(--heading);color:#fff;letter-spacing:.5px}
  .luxury__intro{left:348px;top:46px;width:294px;font-size:6.8px;line-height:1.55;color:#dfe1e8}
  .card{position:absolute;background:var(--paper);padding:6px}
  .card__title{font:700 7.5px/1.2 var(--heading);color:var(--navy)}
  .card__text{font-size:6px;line-height:1.4;color:#4a4d58;margin:2px 0 4px}
  .card .photo{position:relative;width:100%;height:68px}
  .card--suite{left:348px;top:104px;width:92px;height:112px}
  .card--dining{left:446px;top:104px;width:92px;height:112px}
  .card--deck{left:544px;top:104px;width:98px;height:112px}
  .card--pool{left:348px;top:226px;width:190px;height:178px}
  .card--pool .photo{height:138px}
  .luxury__note{left:548px;top:230px;width:94px;font-size:6.6px;line-height:1.55;color:#dfe1e8}

  /* outside left */
  .contact{left:16px;top:20px;width:150px;height:188px;background:rgba(116,119,128,.92);padding:12px 10px;color:#fff;z-index:3;border-right:3px solid var(--paper)}
  .contact__title{font:700 15.5px/1.12 var(--heading);letter-spacing:.4px}
  .person{margin-top:12px}
  .person__name{font:700 9px/1.2 var(--heading);letter-spacing:.4px}
  .person__detail{font-size:6.2px;line-height:1.5;opacity:.9}
  .brand{font:700 10px/1 var(--body);color:var(--navy);letter-spacing:.3px;white-space:nowrap;z-index:3}
  .brand--back{left:184px;top:38px}
  .brand--cover{left:346px;top:34px}
  .party{left:0;top:150px;width:330px;height:277px;clip-path:polygon(0 22%,100% 0,100% 100%,0 100%)}

  /* outside right */
  .river{left:340px;top:72px;width:200px;height:120px;clip-path:polygon(0 10%,100% 0,100% 100%,0 100%)}
  .vines{left:340px;top:198px;width:200px;height:104px}
  .church{left:548px;top:12px;width:104px;height:252px}
  .cover-band{left:330px;top:240px;width:330px;height:187px;background:var(--slate);clip-path:polygon(0 45%,52% 0,100% 22%,100% 100%,0 100%)}
  .cover-accent{left:330px;top:330px;width:120px;height:97px;background:var(--navy);clip-path:polygon(0 0,100% 100%,0 100%)}
  .cover-copy{left:468px;top:318px;width:178px;color:#fff}
  .cover-copy__title{font:700 10px/1.2 var(--heading);letter-spacing:.6px}
  .cover-copy__lede{font-size:6.8px;font-weight:700;line-height:1.4;margin:3px 0}
  .cover-copy__text{font-size:6.3px;line-height:1.5}
</style>
</head>
<body>

<section class="spread spread--inside" aria-label="Inside spread">
  <svg class="decor" width="330" height="427" viewBox="0 0 330 427" aria-hidden="true">
    <polygon points="0,0 150,0 0,48" fill="var(--navy)"/>
    <polygon points="150,0 330,0 330,30" fill="var(--slate-light)"/>
    <polygon points="0,150 18,170 18,427 0,427" fill="var(--navy)"/>
    <polygon points="0,427 330,380 330,427" fill="var(--navy-deep)"/>
  </svg>

  <h2 class="abs included__title">WHAT'S INCLUDED:</h2>
  <ul class="abs included__list">
    <li>Seven nights in a river-view stateroom with a French balcony</li>
    <li>All meals on board, prepared by chefs using local produce</li>
    <li>Fine wines, beer and soft drinks served with lunch and dinner</li>
    <li>Daily guided shore tours in small groups</li>
    <li>Private tasting hosted by your own winemaker</li>
    <li>Welcome and farewell receptions for club members</li>
    <li>Free Wi-Fi, bicycles and onboard fitness classes</li>
    <li>All port charges and gratuities on shore</li>
  </ul>

  <div class="frame food-frame">
    <div class="photo photo--food" style="inset:0" role="img" aria-label="Plated seafood dish with citrus and herbs"></div>
  </div>

  <div class="abs voyage">
    <p class="voyage__text">Sail past terraced vineyards and storybook villages along the Danube.<strong>Vienna · Dürnstein · Melk · Passau</strong></p>
    <div class="photo photo--town" role="img" aria-label="Riverside town with a church tower beneath wooded hills"></div>
  </div>

  <div class="abs luxury"></div>
  <h2 class="abs luxury__title">THE LUXURY OF MORE</h2>
  <p class="abs luxury__intro">Give your wine club members more than a tasting room visit. A river cruise pairs your wines with fine dining, historic towns and the vineyards of Europe, all arranged for you from the first call to the final toast.</p>

  <article class="card card--suite">
    <h3 class="card__title">Spacious Suites</h3>
    <p class="card__text">Twin balconies and river views.</p>
    <div class="photo photo--suite" role="img" aria-label="Bright stateroom with bed and sofa"></div>
  </article>
  <article class="card card--dining">
    <h3 class="card__title">Chef's Table</h3>
    <p class="card__text">A tasting menu paired with wine.</p>
    <div class="photo photo--dining" role="img" aria-label="Gourmet dish served at the chef's table"></div>
  </article>
  <article class="card card--deck">
    <h3 class="card__title">Sun Deck Pool</h3>
    <p class="card__text">Swim as the vineyards drift by.</p>
    <div class="photo photo--suite" role="img" aria-label="Ship lounge with river views"></div>
  </article>
  <article class="card card--pool">
    <div class="photo photo--pool" role="img" aria-label="Heated pool on the ship's sun deck"></div>
  </article>
  <p class="abs luxury__note">Every sailing on Orvel Riverlines includes guided tours, wine and dinner.</p>

  <div class="fold"></div>
</section>

<section class="spread spread--outside" aria-label="Outside spread">
  <svg class="decor" width="660" height="427" viewBox="0 0 660 427" aria-hidden="true">
    <polygon points="0,0 330,0 330,120 170,40 0,110" fill="var(--mist)"/>
    <polygon points="170,40 330,120 330,150" fill="var(--slate-light)"/>
    <polygon points="330,0 560,0 330,60" fill="var(--mist)"/>
  </svg>

  <div class="abs contact">
    <h2 class="contact__title">FOR GROUP INQUIRIES, CONTACT:</h2>
    <div class="person">
      <p class="person__name">DORIAN WEXLEY</p>
      <p class="person__detail">Group Sales Director<br>555-014-2290<br>dorian@brindlecove.com</p>
    </div>
    <div class="person">
      <p class="person__name">TESSA MARLOW</p>
      <p class="person__detail">Travel Advisor<br>555-014-3381<br>tessa@brindlecove.com</p>
    </div>
  </div>

  <p class="abs brand brand--back">Brindlecove Travel</p>

  <div class="photo photo--party party" role="img" aria-label="Guests celebrating around the ship's pool deck"></div>

  <p class="abs brand brand--cover">Brindlecove Travel</p>

  <div class="photo photo--river river" role="img" aria-label="River town seen across the water"></div>
  <div class="photo photo--vines vines" role="img" aria-label="Vineyard rows on a hillside"></div>
  <div class="photo photo--church church" role="img" aria-label="Church tower above a village"></div>

  <div class="abs cover-band"></div>
  <div class="abs cover-accent"></div>
  <div class="abs cover-copy">
    <h1 class="cover-copy__title">WINE AND RIVER CRUISING</h1>
    <p class="cover-copy__lede">Share your wines with the people who love them most.</p>
    <p class="cover-copy__text">Invite your club members on a private river voyage through Europe's great wine regions, with tastings, cellar tours and dinners hosted by your winery.</p>
  </div>

  <div class="fold"></div>
</section>

</body>
</html>
```